Honey apple cider vinegar label

organic food company need a contemporary honey apple cider vinegar and honey vinegar label, natural GMP logo HACCP LOgo
label detail height :140mm Width:80mm
ingredient: honey, apple cider vinegar and water, free from artificial color & preservative
Shelf Life: 3 years
Net weight 400ml
Storage : store in cool place , do not expose to sunlight
instruction for use: add 20ml to a full glass of water 3, times a days before meal, stop consuming if allergies happen
certification, GMP HACCP, Halal, natural product

Target Market(s)

health conscious group

Requirements
Must have
• modern feel, honey and apple picture

```html
<!DOCTYPE html>
<html lang="en">
<head>
<meta charset="utf-8">
<title>Verdalo Apple Cider Vinegar with Honey – Label</title>
<link rel="stylesheet" href="https://fonts.googleapis.com/css2?family=Open+Sans:ital,wght@0,400;0,600;0,700;1,600&family=Roboto+Slab:wght@800;900&display=swap">
<style>
  :root {
    --plum: #2f1c45;
    --olive: #4a5212;
    --olive-dark: #3e4412;
    --honey: #f5b70a;
    --honey-band: #f6b60c;
    --ink: #1c1c1c;
    --paper: #ffffff;
    --apple-red: #9e1a1c;
    --apple-deep: #5e0d0f;
    --badge-blue: #1f4d8c;
    --badge-green: #3aa435;
  }
  * { margin: 0; padding: 0; box-sizing: border-box; }
  html, body { width: 724px; height: 1200px; overflow: hidden; background: var(--paper); }
  .label {
    position: relative;
    width: 724px;
    height: 1200px;
    background: var(--paper);
    font-family: "Open Sans", Arial, sans-serif;
    color: var(--ink);
  }
  .brand-dot {
    position: absolute;
    left: 292px; top: 60px;
    width: 140px; height: 140px;
    border-radius: 50%;
    background: var(--honey);
  }
  .brand-name {
    position: absolute;
    left: 0; right: 0; top: 300px;
    text-align: center;
    font-family: "Open Sans", Arial, sans-serif;
    font-weight: 700;
    font-size: 128px;
    line-height: 150px;
    letter-spacing: 2px;
    color: var(--plum);
  }
  .brand-rule {
    position: absolute;
    left: 69px; top: 455px;
    width: 605px; height: 7px;
    background: var(--honey);
  }
  .product-title {
    position: absolute;
    left: 69px; width: 605px;
    font-family: "Roboto Slab", Georgia, serif;
    font-weight: 900;
    color: var(--olive);
    text-align: center;
    white-space: nowrap;
  }
  .title-apple { top: 478px; font-size: 80px; line-height: 84px; letter-spacing: -2px; word-spacing: 28px; }
  .title-vinegar { top: 556px; font-size: 126px; line-height: 130px; letter-spacing: -5px; }
  .title-with { top: 690px; font-size: 96px; line-height: 110px; letter-spacing: -3px; }
  .title-with .honey-word { color: var(--honey); font-size: 110px; }

  .certs { position: absolute; left: 30px; top: 792px; }
  .cert { position: absolute; }
  .cert-haccp { left: 3px; top: 4px; width: 60px; height: 60px; border-radius: 50%; background: var(--badge-blue); }
  .cert-gmp { left: 97px; top: 4px; width: 60px; height: 60px; border-radius: 50%; border: 3px solid #cfcfcf; background: var(--badge-green); }
  .cert-halal { left: 196px; top: 10px; width: 88px; height: 44px; border-radius: 6px; background: var(--badge-green); }

  .apple-art {
    position: absolute;
    left: 188px; top: 822px;
    width: 334px; height: 214px;
    border-radius: 48% 48% 0 0 / 60% 60% 0 0;
    background: radial-gradient(ellipse at 40% 35%, #d0542a 0%, var(--apple-red) 45%, var(--apple-deep) 100%);
  }
  .net-weight {
    position: absolute;
    left: 313px; top: 958px;
    width: 160px; height: 78px;
    border-radius: 80px 80px 0 0;
    background: var(--olive-dark);
    color: var(--honey);
    font-weight: 600;
    font-size: 18px;
    line-height: 22px;
    text-align: center;
    padding-top: 22px;
  }
  .free-from {
    position: absolute;
    right: 0; top: 815px;
    width: 222px; height: 102px;
    border-radius: 52px 0 0 52px;
    background: var(--plum);
    color: var(--paper);
    font-weight: 600;
    font-size: 18px;
    line-height: 27px;
    text-align: center;
    padding: 22px 0 0 14px;
  }
  .storage {
    position: absolute;
    left: 28px; top: 878px;
    font-weight: 600;
    font-size: 20.5px;
    line-height: 29.5px;
  }
  .shelf-life {
    position: absolute;
    left: 545px; top: 950px;
    width: 160px;
    text-align: center;
    font-weight: 700;
    font-size: 23px;
    line-height: 30px;
  }
  .info-band {
    position: absolute;
    left: 0; right: 0; top: 1036px; bottom: 0;
    background: var(--honey-band);
    padding: 18px 0 0 48px;
  }
  .ingredients { font-weight: 600; font-size: 24.5px; line-height: 34px; }
  .instructions { font-style: italic; font-weight: 600; font-size: 19.5px; line-height: 30px; margin-top: 4px; }
  .instructions ol { list-style: none; }
</style>
</head>
<body>
<main class="label">
  <div class="brand-dot"></div>
  <h1 class="brand-name">verdalo</h1>
  <div class="brand-rule"></div>

  <div class="product-title title-apple">APPLE CIDER</div>
  <div class="product-title title-vinegar">VINEGAR</div>
  <div class="product-title title-with">with <span class="honey-word">Honey</span></div>

  <div class="certs" aria-label="Certifications">
    <div class="cert cert-haccp"></div>
    <div class="cert cert-gmp"></div>
    <div class="cert cert-halal"></div>
  </div>

  <div class="apple-art" role="img" aria-label="Red apple with golden honey dripping over it"></div>
  <div class="net-weight">Net Weight<br>400ml</div>

  <div class="free-from">No Artificial Color<br>&amp; Preservative</div>

  <p class="storage">Storage :<br>Store in Cool<br>Dry Place. Do<br>Not Expose<br>To Sunlight</p>

  <p class="shelf-life">Shelf Life :<br>3 Years</p>

  <section class="info-band">
    <p class="ingredients">Ingredient: Honey, Apple Cider Vinegar and Water</p>
    <div class="instructions">
      <p>Instruction for Use:</p>
      <ol>
        <li>1. Add 20ml to a full glass of water 3 times a day before meal.</li>
        <li>2&nbsp; Stop consuming if allergies happen.</li>
      </ol>
    </div>
  </section>
</main>
</body>
</html>
```